Dalton Power Supply, Inc. Business Card Design

We are an Electrical Distributor looking for a Modern, Professional Business Card design.

Target Market(s)

Residential Commercial Industrial

Industry/Entity Type

Electrical

Contact Information for Business Card

Dalton Power Supply, Inc.
418 Maple Ridge Lane
Brookvale, NC 27514
555-214-7630
555-214-8842 Fax
daltonpower@brightmail-example.net

```html
<!DOCTYPE html>
<html lang="en">
<head>
<meta charset="utf-8">
<title>Dalton Power Supply, Inc. – Business Card</title>
<link href="https://fonts.googleapis.com/css2?family=Jost:wght@600;700&family=Open+Sans:wght@400;600&display=swap" rel="stylesheet">
<style>
  :root {
    --page: #f0f0f0;
    --card: #fafafa;
    --red: #e3222a;
    --red-light: #f4604a;
    --blue: #2f3f98;
    --blue-light: #4d6fc4;
    --ink: #3a3a3a;
    --ink-soft: #474747;
    --icon: #111111;
    --bevel-top: #f2f3f8;
    --bevel-left: #d3d7e3;
    --bevel-right: #c4c8d5;
    --bevel-bottom: #bcbfcb;
  }
  * { margin: 0; padding: 0; box-sizing: border-box; }
  html, body { width: 1200px; height: 720px; overflow: hidden; background: var(--page); }
  .canvas { position: relative; width: 1200px; height: 720px; }
  .card { position: absolute; left: 59px; top: 51px; width: 1082px; height: 618px; background: var(--card); overflow: hidden; }

  .stripe { position: absolute; }
  .stripe--top { left: 104px; top: 0; width: 322px; height: 31px; border-radius: 0 0 22px 22px;
    background: linear-gradient(to bottom, var(--red) 0%, var(--red-light) 30%, var(--red) 48%, var(--blue-light) 55%, var(--blue) 100%); }
  .stripe--bottom { left: 104px; bottom: 0; width: 322px; height: 31px; border-radius: 22px 22px 0 0;
    background: linear-gradient(to bottom, var(--blue) 0%, var(--blue-light) 45%, var(--red) 52%, var(--red-light) 75%, var(--red) 100%); }
  .stripe--side { right: 0; top: 147px; width: 32px; height: 322px; border-radius: 22px 0 0 22px;
    background: linear-gradient(to right, var(--blue) 0%, var(--blue-light) 45%, var(--red) 52%, var(--red-light) 75%, var(--red) 100%); }

  .identity { position: absolute; left: 85px; width: 360px; text-align: center; }
  .company { top: 141px; font-family: "Jost", sans-serif; font-weight: 700; font-size: 39px; line-height: 50px; color: var(--red); letter-spacing: 0.5px; text-transform: uppercase; }
  .divider { position: absolute; left: 222px; top: 311px; width: 97px; height: 3px; background: var(--icon); }
  .person { top: 384px; }
  .person__name { font-family: "Jost", sans-serif; font-weight: 700; font-size: 38px; line-height: 48px; color: var(--red); letter-spacing: 0.5px; text-transform: uppercase; }
  .person__role { font-family: "Open Sans", sans-serif; font-weight: 600; font-size: 28px; line-height: 36px; color: var(--ink); letter-spacing: -0.8px; text-transform: uppercase; }

  .frame { position: absolute; left: 541px; top: 34px; width: 491px; height: 550px; }

  .contacts { position: absolute; left: 598px; top: 0; list-style: none; font-family: "Open Sans", sans-serif; color: var(--ink-soft); }
  .contact { position: absolute; left: 0; display: flex; align-items: flex-start; white-space: nowrap; }
  .contact__icon { width: 24px; height: 24px; margin-right: 13px; flex: none; }
  .contact__text { font-size: 22px; line-height: 30px; }
  .contact--phone { top: 158px; }
  .contact--fax { top: 228px; }
  .contact--email { top: 296px; }
  .contact--email .contact__text { font-size: 19.5px; }
  .contact--address { top: 366px; }
  .contact--address .contact__text { line-height: 30.5px; }
  .contact-rule { position: absolute; left: 0; width: 32px; height: 2px; background: var(--ink-soft); }
</style>
</head>
<body>
<div class="canvas">
  <div class="card">
    <div class="stripe stripe--top"></div>
    <div class="stripe stripe--bottom"></div>
    <div class="stripe stripe--side"></div>

    <h1 class="identity company">Dalton Power<br>Supply, Inc.</h1>
    <div class="divider"></div>
    <div class="identity person">
      <p class="person__name">Thomas Reed</p>
      <p class="person__role">Executive Manager</p>
    </div>

    <svg class="frame" viewBox="0 0 491 550" aria-hidden="true">
      <polygon points="0,0 491,0 458,49 33,49" fill="var(--bevel-top)"/>
      <polygon points="0,0 33,49 33,501 0,550" fill="var(--bevel-left)"/>
      <polygon points="491,0 491,550 458,501 458,49" fill="var(--bevel-right)"/>
      <polygon points="0,550 33,501 458,501 491,550" fill="var(--bevel-bottom)"/>
      <rect x="33" y="49" width="425" height="452" fill="var(--card)"/>
    </svg>

    <ul class="contacts">
      <li class="contact contact--phone">
        <svg class="contact__icon" viewBox="0 0 24 24" aria-hidden="true"><path fill="var(--icon)" d="M6.6 3.5l2.6 3.4c.4.5.3 1.2-.1 1.6L7.7 9.9c1.2 2.6 3.4 4.9 6.1 6.2l1.4-1.4c.4-.4 1.1-.5 1.6-.1l3.4 2.6c.5.4.6 1.1.2 1.6l-1.6 2c-.6.7-1.5 1-2.4.8C9.9 20 4.1 14.2 2.6 7.8c-.2-.9.1-1.8.8-2.4l1.6-1.6c.5-.5 1.2-.5 1.6-.3z"/></svg>
        <span class="contact__text">555-214-7630</span>
      </li>
      <li class="contact-rule" style="top:207px"></li>
      <li class="contact contact--fax">
        <svg class="contact__icon" viewBox="0 0 24 24" aria-hidden="true"><path fill="var(--icon)" d="M6 2h12v6H6z M3 9h18c1 0 2 1 2 2v9c0 1-1 2-2 2H3c-1 0-2-1-2-2v-9c0-1 1-2 2-2z"/><path fill="var(--card)" d="M7.5 3.5h9v1.2h-9zM7.5 5.8h9V7h-9zM6 15c0-2.2 2.7-3.2 6-3.2s6 1 6 3.2v1.5h-3v-1.5H9v1.5H6z"/></svg>
        <span class="contact__text">555-214-8842</span>
      </li>
      <li class="contact-rule" style="top:277px"></li>
      <li class="contact contact--email">
        <svg class="contact__icon" viewBox="0 0 24 24" aria-hidden="true" style="margin-top:4px"><path fill="var(--icon)" d="M2 5h20v2.2l-10 6-10-6z M2 9.5l10 6 10-6V19H2z"/></svg>
        <span class="contact__text">daltonpower@brightmail-example.net</span>
      </li>
      <li class="contact-rule" style="top:345px"></li>
      <li class="contact contact--address">
        <svg class="contact__icon" viewBox="0 0 24 24" aria-hidden="true" style="width:24px;height:30px"><path fill="var(--icon)" d="M12 1a7.5 7.5 0 0 0-7.5 7.5C4.5 14 12 23 12 23s7.5-9 7.5-14.5A7.5 7.5 0 0 0 12 1zm0 10.3a2.8 2.8 0 1 1 0-5.6 2.8 2.8 0 0 1 0 5.6z"/></svg>
        <span class="contact__text">Dalton Power Supply, Inc.<br>418 Maple Ridge Lane<br>Brookvale, NC 27514</span>
      </li>
    </ul>
  </div>
</div>
</body>
</html>
```